I am looking for a stand-out cover that sings out to new parents. The category is very pastel with limited compelling covers that would make me want to buy a book. This book will be used often in the first 12 months of baby's life - so must be strong enough to sit on the bedside table or on the coffee table to inspire reading. It will be a popular gift - so needs to look credible, "pick-up-able" and loveable.

The Book Title is - The Cradle Compass to Infancy's Opening Seasons: Grounded, Research-Led Methods on Rest, Nourishment, Protection plus Growing Assurance
The Size is - 8.5 x 11 in
Book description to be provided to final design for inclusion
Some examples of book covers in this category attached. Thanks

```html
<!DOCTYPE html>
<html lang="en">
<head>
<meta charset="utf-8">
<title>The Cradle Compass to Infancy's Opening Seasons — Book Cover</title>
<link rel="stylesheet" href="https://fonts.googleapis.com/css2?family=Cinzel:wght@600;700&family=Poppins:wght@400&display=swap">
<style>
  :root {
    --paper: #fcf9f7;
    --blush: #f2dfd6;
    --gold-light: #c9a040;
    --gold-mid: #9a7426;
    --gold-dark: #4e3810;
    --ink: #1c1a18;
    --sage: #a9a08a;
    --sage-soft: #cbc3b0;
    --peach: #ecd3c0;
    --wicker: #d8b9a8;
    --wicker-deep: #b8998a;
    --linen: #f1f1e8;
  }
  * { margin: 0; padding: 0; box-sizing: border-box; }
  html, body { width: 875px; height: 1200px; overflow: hidden; background: var(--paper); }
  .cover {
    position: relative;
    width: 875px;
    height: 1200px;
    overflow: hidden;
    background:
      radial-gradient(ellipse 360px 260px at 820px 90px, rgba(242,223,214,0.75), transparent 70%),
      radial-gradient(ellipse 300px 240px at 80px 1120px, rgba(242,223,214,0.7), transparent 70%),
      radial-gradient(ellipse 260px 200px at 120px 80px, rgba(240,232,226,0.6), transparent 70%),
      var(--paper);
  }
  .art { position: absolute; }
  .art--branch-top {
    left: 541px; top: 0; width: 334px; height: 227px;
    border-radius: 10% 0 50% 60% / 10% 0 60% 70%;
    background: linear-gradient(155deg, rgba(169,160,138,0.15) 0%, var(--sage-soft) 30%, var(--peach) 55%, var(--sage) 78%, rgba(236,211,192,0.35) 100%);
    opacity: 0.85;
  }
  .art--sprig {
    left: 114px; top: 474px; width: 160px; height: 320px;
    border-radius: 60% 40% 50% 50% / 40% 40% 60% 60%;
    background: linear-gradient(200deg, var(--sage-soft) 0%, var(--peach) 45%, var(--sage) 80%, rgba(169,160,138,0.3) 100%);
    opacity: 0.8;
  }
  .art--basket {
    left: 236px; top: 529px; width: 639px; height: 553px;
    border-radius: 38% 32% 30% 34% / 30% 28% 40% 46%;
    background: linear-gradient(180deg,
      var(--peach) 0%,
      var(--linen) 14%,
      #f4f2ea 42%,
      #ebe6dc 56%,
      var(--wicker) 68%,
      var(--wicker-deep) 84%,
      #e3cfc4 100%);
    box-shadow: 0 26px 30px -14px rgba(120,100,90,0.25);
  }
  .art--branch-left {
    left: 0; top: 740px; width: 517px; height: 442px;
    border-radius: 20% 70% 70% 30% / 30% 60% 70% 60%;
    background: linear-gradient(160deg, rgba(169,160,138,0.35) 0%, var(--sage) 25%, var(--peach) 48%, var(--sage-soft) 68%, rgba(236,211,192,0.55) 88%, rgba(236,211,192,0) 100%);
    opacity: 0.85;
  }
  .title {
    position: absolute;
    left: 92px; top: 0;
    width: 440px; height: 370px;
    font-family: "Cinzel", serif;
    font-weight: 700;
    line-height: 1;
    white-space: nowrap;
  }
  .title span {
    position: absolute;
    left: 0;
    display: block;
    background: linear-gradient(100deg, var(--gold-light) 0%, var(--gold-mid) 30%, var(--gold-dark) 55%, var(--gold-mid) 78%, var(--gold-light) 100%);
    -webkit-background-clip: text;
    background-clip: text;
    color: transparent;
  }
  .title__lead { top: 88px; font-size: 31px; letter-spacing: 0.5px; }
  .title__main { top: 132px; font-size: 76px; }
  .title__big  { top: 208px; font-size: 90px; }
  .title__tail { top: 316px; font-size: 33px; letter-spacing: 0.5px; }
  .subtitle {
    position: absolute;
    left: 93px; top: 384px;
    font-family: "Poppins", sans-serif;
    font-size: 16.5px;
    line-height: 1.6;
    color: var(--ink);
  }
  .author {
    position: absolute;
    left: 528px; top: 1120px;
    font-family: "Cinzel", serif;
    font-weight: 700;
    font-size: 27px;
    letter-spacing: 0.5px;
    background: linear-gradient(100deg, var(--gold-light), var(--gold-dark) 55%, var(--gold-mid));
    -webkit-background-clip: text;
    background-clip: text;
    color: transparent;
    white-space: nowrap;
  }
</style>
</head>
<body>
  <main class="cover">
    <div class="art art--branch-top" role="img" aria-label="Watercolour branch of sage and blush leaves reaching in from the top edge"></div>
    <div class="art art--basket" role="img" aria-label="Watercolour illustration of a sleeping baby wrapped in a cream blanket inside a wicker basket"></div>
    <div class="art art--sprig" role="img" aria-label="Watercolour sprig of sage and peach leaves beside the basket"></div>
    <div class="art art--branch-left" role="img" aria-label="Watercolour trailing branch of sage and peach leaves across the lower left"></div>

    <h1 class="title">
      <span class="title__lead">THE CRADLE COMPASS TO</span>
      <span class="title__main">INFANCY'S</span>
      <span class="title__big">OPENING</span>
      <span class="title__tail">SEASONS</span>
    </h1>
    <p class="subtitle">Grounded, Research-Led Methods on Rest,<br>Nourishment, Protection plus Growing Assurance</p>

    <p class="author">MARTIN ASHGROVE</p>
  </main>
</body>
</html>
```